Black Friday Sale Social Media Graphics

Focusing on Black Friday Graphics for each of the pics attached.  So need the product pics turned into  social media graphics (square size). For the color scheme of the graphics, they should all be complementary to the product colors.
You can add any of the stock photography attached but none are required. I mainly need BOLD text that says:
Black Friday Sale
Up to $15 Off
If you wanted to add smaller text, these headlines can work:
1.	Burn Belly Fat Fast!
2.	Double Your Weight Loss With Our Supplements!
3.	Lose Weight Naturally: Ditch the Prescription Pills & Needles!
4.	Tired of Stubborn Belly Fat? Discover What Works!
5.	Melt Away Belly Fat Faster with Our Supplements!
6.	Struggling to Lose Weight? Discover the Ultimate Solution!
7.	Ready to Burn Fat Faster?

Target Market(s)
women trying to lose weight
Industry/Entity Type
health and wellness
Requirements
Must have
- the product pics attached

Nice to have
- Bold text that says: Black Friday Sale

```html
<!DOCTYPE html>
<html lang="en">
<head>
<meta charset="UTF-8">
<title>Black Friday Sale – Burn Belly Fat Fast</title>
<link rel="stylesheet" href="https://fonts.googleapis.com/css2?family=Archivo+Black&family=Montserrat:wght@700;800;900&display=swap">
<style>
  :root {
    --ink-black: #0b0b0b;
    --satin-dark: #1a1a1a;
    --satin-mid: #2c2c2c;
    --white: #ffffff;
    --tag-red: #e8242c;
    --bottle-white: #eeeeee;
    --bottle-shadow: #bdbdbd;
  }
  * { margin: 0; padding: 0; box-sizing: border-box; }
  html, body {
    width: 1200px;
    height: 1006px;
    overflow: hidden;
    background: var(--ink-black);
  }
  .promo-canvas {
    position: relative;
    width: 1200px;
    height: 1006px;
    overflow: hidden;
  }
  .satin-backdrop {
    position: absolute;
    inset: 0;
    background:
      radial-gradient(ellipse 60% 40% at 25% 30%, var(--satin-mid) 0%, transparent 70%),
      radial-gradient(ellipse 50% 35% at 80% 70%, var(--satin-mid) 0%, transparent 70%),
      linear-gradient(160deg, var(--satin-dark) 0%, var(--ink-black) 55%, var(--satin-dark) 100%);
  }
  .headline {
    position: absolute;
    left: 0;
    width: 100%;
    text-align: center;
    font-family: "Archivo Black", "Montserrat", sans-serif;
    line-height: 1;
    color: var(--white);
  }
  .headline--solid {
    top: 168px;
    left: 4px;
    font-size: 206px;
    letter-spacing: 2px;
  }
  .headline--outline {
    top: 313px;
    left: 42px;
    font-size: 220px;
    letter-spacing: 2px;
    color: transparent;
    -webkit-text-stroke: 4px var(--white);
  }
  .product-lineup {
    position: absolute;
    left: 208px;
    top: 468px;
    width: 625px;
    height: 332px;
    border-radius: 28px 28px 14px 14px;
    background: linear-gradient(180deg, var(--bottle-white) 0%, #f7f7f7 50%, var(--bottle-shadow) 100%);
  }
  .sale-tag {
    position: absolute;
    left: 0;
    top: 0;
    width: 1200px;
    height: 1006px;
    pointer-events: none;
  }
  .sale-tag text {
    fill: var(--white);
    font-family: "Montserrat", sans-serif;
  }
  .tag-small { font-size: 20px; font-weight: 800; }
  .tag-big { font-size: 66px; font-weight: 900; }
  .tag-off { font-size: 34px; font-weight: 900; }
  .tagline {
    position: absolute;
    left: 0;
    width: 100%;
    top: 932px;
    text-align: center;
    font-family: "Montserrat", sans-serif;
    font-weight: 800;
    font-size: 30px;
    letter-spacing: 10px;
    color: var(--white);
  }
</style>
</head>
<body>
<main class="promo-canvas">
  <div class="satin-backdrop" role="img" aria-label="Draped black satin fabric background"></div>

  <h1 class="headline headline--solid">BLACK</h1>
  <div class="headline headline--outline">FRIDAY</div>

  <div class="product-lineup" role="img" aria-label="Product photo of four white supplement bottles with colored labels standing side by side"></div>

  <svg class="sale-tag" viewBox="0 0 1200 1006" aria-label="Up to 15% off">
    <path d="M780 510 C 810 480, 845 500, 880 560" fill="none" stroke="var(--white)" stroke-width="2"/>
    <g transform="translate(978 625) rotate(20)">
      <path d="M-120 -58 L125 -58 L125 58 L-120 58 L-158 0 Z" fill="var(--tag-red)"/>
      <circle cx="-126" cy="0" r="8" fill="var(--ink-black)"/>
      <text class="tag-small" x="-92" y="-30">UP TO</text>
      <text class="tag-big" x="-98" y="30">15%</text>
      <text class="tag-off" x="52" y="34">Off</text>
    </g>
  </svg>

  <p class="tagline">BURN BELLY FAT FAST!</p>
</main>
</body>
</html>
```